Assisted living facility needs a business card design

We need a business card design for an assisted living facility in Los Angeles. We have a logo selected but we would like a business card design that will leave a lasting impression on families looking to place their elderly loved ones in our care as well as on other facility providers who may refer their elderly residents to our facility.

```html
<!DOCTYPE html>
<html lang="en">
<head>
<meta charset="utf-8">
<title>Kingsbury Haven – Business Card</title>
<link href="https://fonts.googleapis.com/css2?family=Arimo:wght@400;700&display=swap" rel="stylesheet">
<style>
  :root {
    --backdrop: #e4e4e6;
    --card: #fbfbfb;
    --brand-blue: #1a6fbd;
    --ink: #1f1f1f;
    --muted: #555555;
    --rule: #c9c9c9;
  }
  * { box-sizing: border-box; margin: 0; padding: 0; }
  html, body {
    width: 1200px; height: 768px; overflow: hidden;
    background: var(--backdrop);
    font-family: "Arimo", Arial, sans-serif;
  }
  .canvas {
    width: 1200px; height: 768px;
    display: flex; align-items: center; justify-content: center; gap: 48px;
  }
  .card {
    position: relative;
    width: 525px; height: 300px;
    background: var(--card);
    border-radius: 22px;
    box-shadow: 0 6px 18px rgba(0,0,0,.12);
  }
  .brand-name {
    color: var(--brand-blue);
    font-weight: 400;
    letter-spacing: .04em;
    text-transform: uppercase;
    white-space: nowrap;
  }
  .card--back { display: flex; align-items: center; justify-content: center; }
  .card--back .brand-name { font-size: 40px; }

  .card--front .brand-name {
    position: absolute; left: 44px; top: 40px;
    font-size: 25px;
  }
  .contact {
    position: absolute; left: 300px; top: 150px;
    padding-left: 14px;
    border-left: 1px solid var(--rule);
    color: var(--ink);
  }
  .contact__name { color: var(--brand-blue); font-weight: 700; font-size: 20px; line-height: 1.1; }
  .contact__role { color: var(--muted); font-size: 13px; margin-bottom: 10px; }
  .contact__address { font-size: 13.5px; line-height: 1.3; margin-bottom: 6px; }
  .contact__line { display: flex; align-items: center; gap: 8px; font-size: 13.5px; line-height: 1.4; }
  .contact__line svg { width: 11px; height: 11px; fill: var(--brand-blue); flex: none; }
</style>
</head>
<body>
<main class="canvas">
  <section class="card card--back" aria-label="Card back">
    <p class="brand-name">Kingsbury Haven</p>
  </section>

  <section class="card card--front" aria-label="Card front">
    <p class="brand-name">Kingsbury Haven</p>
    <div class="contact">
      <p class="contact__name">Thomas Reed</p>
      <p class="contact__role">President</p>
      <p class="contact__address">4127 Larkspur Avenue<br>Glendale, CA 91204</p>
      <p class="contact__line">
        <svg viewBox="0 0 24 24" aria-hidden="true"><path d="M6.6 10.8a15.1 15.1 0 0 0 6.6 6.6l2.2-2.2c.3-.3.7-.4 1-.2 1.1.4 2.3.6 3.6.6.6 0 1 .4 1 1V20c0 .6-.4 1-1 1A17 17 0 0 1 3 4c0-.6.4-1 1-1h3.5c.6 0 1 .4 1 1 0 1.3.2 2.5.6 3.6.1.3 0 .7-.2 1z"/></svg>
        (555) 8142-6307
      </p>
      <p class="contact__line">
        <svg viewBox="0 0 24 24" aria-hidden="true"><path d="M2 5h20v14H2zm2 2v.5l8 5 8-5V7l-8 5z"/></svg>
        name@kingsburyhaven.com
      </p>
      <p class="contact__line">
        <svg viewBox="0 0 24 24" aria-hidden="true"><circle cx="12" cy="12" r="10"/></svg>
        www.kingsburyhaven.com
      </p>
    </div>
  </section>
</main>
</body>
</html>
```